Perfume packaging design

We are a company producing perfumery and deodorants in the upper mass market segment (semi-selective). We need a packaging design for our new fragrance for women called Moon Petal. You will find attached a picture of the chosen bottle and cap along with specification.

The fragrance is modern and delicate. It is sweet with floral accent and notes of mandarin, rose, peach.

Suitable for evening perfume as well as casual daily.

Looking for:
1. logo - "Moon Petal" on bottle and packaging
2. Color of the perfume
3. Design of the carton box

Product is 100ml eau de perfume for women.

Target Market(s)

Target market is Eastern Europe and middle east

Women
Age 30-45
Price range - semi-selective
Sales channels - perfumeries, drug stores and online

Industry/Entity Type

It Company

Requirements
Must have
• Packaging - carton
Perfume should be colored
Embosing
Nice to have
• Golden hot stamping or other golden element

```html
<!DOCTYPE html>
<html lang="en">
<head>
<meta charset="utf-8">
<title>Moon Petal – Carton Dieline</title>
<link rel="stylesheet" href="https://fonts.googleapis.com/css2?family=Mulish:wght@400;600&display=swap">
<style>
  :root {
    --paper: #ffffff;
    --navy: #131a2f;
    --gold-deep: #c58620;
    --gold-light: #f2b838;
    --ink-light: #ffffff;
  }
  html, body {
    margin: 0;
    padding: 0;
    width: 1200px;
    height: 1000px;
    overflow: hidden;
    background: var(--paper);
  }
  .canvas {
    position: relative;
    width: 1200px;
    height: 1000px;
    font-family: "Mulish", Arial, sans-serif;
    color: var(--ink-light);
  }
  .dieline {
    position: absolute;
    inset: 0;
  }
  .panel-navy { fill: var(--navy); }
  .gold-frame { fill: none; stroke: url(#goldFoil); stroke-width: 5; }
  .ornament {
    position: absolute;
    height: 12px;
    background: linear-gradient(90deg, transparent, var(--gold-deep) 15%, var(--gold-light) 50%, var(--gold-deep) 85%, transparent);
    opacity: 0.85;
    border-radius: 6px;
  }
  .story-text {
    position: absolute;
    left: 397px;
    top: 502px;
    width: 190px;
    margin: 0;
    font-size: 9.4px;
    line-height: 10.6px;
    text-align: center;
  }
  .wordmark {
    position: absolute;
    left: 884px;
    top: 499px;
    width: 256px;
    margin: 0;
    text-align: center;
    font-size: 22px;
    font-weight: 400;
    letter-spacing: 0.5px;
    color: var(--ink-light);
  }
  .product-type {
    position: absolute;
    left: 884px;
    top: 665px;
    width: 256px;
    margin: 0;
    text-align: center;
    font-size: 8.5px;
    line-height: 11px;
    letter-spacing: 0.3px;
  }
  .volume {
    position: absolute;
    top: 725px;
    margin: 0;
    font-size: 8.5px;
  }
  .volume-ml { left: 893px; }
  .volume-oz { right: 72px; }
</style>
</head>
<body>
<main class="canvas">
  <svg class="dieline" width="1200" height="1000" viewBox="0 0 1200 1000" aria-hidden="true">
    <defs>
      <linearGradient id="goldFoil" x1="0" y1="0" x2="1" y2="1">
        <stop offset="0" stop-color="#c58620"/>
        <stop offset="0.5" stop-color="#f2b838"/>
        <stop offset="1" stop-color="#c58620"/>
      </linearGradient>
    </defs>

    <!-- top lid -->
    <polygon class="panel-navy" points="386,80 595,80 623,158 675,185 675,395 623,420 362,420 310,395 310,185 360,158"/>

    <!-- glue tab and left side panel -->
    <polygon class="panel-navy" points="45,433 97,420 362,420 362,748 265,827 333,880 123,880 175,827 97,746 45,733"/>

    <!-- back panel with bottom flap -->
    <rect class="panel-navy" x="362" y="420" width="260" height="328"/>
    <polygon class="panel-navy" points="362,748 622,748 622,880 521,880 521,827 440,827 440,880 362,880"/>

    <!-- right side panel -->
    <polygon class="panel-navy" points="622,420 882,420 882,748 790,827 858,880 647,880 698,827 622,748"/>

    <!-- front panel with bottom flap -->
    <rect class="panel-navy" x="882" y="420" width="261" height="325"/>
    <polygon class="panel-navy" points="882,745 1143,745 1143,880 1042,880 1042,827 960,827 960,880 882,880"/>

    <!-- gold foil frames -->
    <rect class="gold-frame" x="365.5" y="423.5" width="254" height="320"/>
    <rect class="gold-frame" x="885.5" y="423.5" width="253" height="320"/>
  </svg>

  <!-- back panel -->
  <div class="ornament" style="left:430px; top:480px; width:123px;" role="img" aria-label="Gold foil scroll flourish"></div>
  <p class="story-text">Lorem ipsum dolor sit amet, consectetuer adipiscing elit, sed diam nonummy nibh euismod tincidunt ut laoreet dolore magna aliquam erat volutpat. Ut wisi enim ad minim veniam, quis nostrud exerci tation ullamcorper suscipit lobortis nisl ut aliquip ex ea commodo consequat. Duis autem vel eum iriure dolor in hendrerit in vulputate velit esse molestie consequat, vel illum dolore eu feugiat.</p>
  <div class="ornament" style="left:430px; top:630px; width:123px;" role="img" aria-label="Gold foil scroll flourish"></div>

  <!-- front panel -->
  <div class="ornament" style="left:948px; top:483px; width:126px;" role="img" aria-label="Gold foil scroll flourish"></div>
  <h1 class="wordmark">Moon Petal</h1>
  <div class="ornament" style="left:948px; top:532px; width:126px;" role="img" aria-label="Gold foil scroll flourish"></div>
  <p class="product-type">EAU DE PARFUM<br>NATURAL SPRAY</p>
  <p class="volume volume-ml">100ml</p>
  <p class="volume volume-oz">3.4 fl oz</p>
</main>
</body>
</html>
```